KLD Business card design

we are a new real estate agent, mainly selling off the plan projects, most of our client are overseas buyers. Please design a letter mark logo with "K L D" which is the name of the company. and the back side of the business card, i would like to have the logo on it. I was thinking to use "monoton" font for the "K L D" logo,and use "red, yellow, blue" colour in order on each letter. please give me some opinions. or design a better one for me.

Reason: I would like to reduce the deadline to 9/7/13 , thanks

Please add job title: Licensed Real Estate Agent

Industry/Entity Type

Real Estate

Contact Information for Business Card

Company Name: Marlowgate Property Collective Pty. Ltd. ,Name: Daniel Roke , Address: PO Box 732 Wendrick BC NSW 1593 , mob: 0437 592 046 , Phone: 02 8364 5917 Email: daniel.roke@marlowgatepc.com.au

Logo styles of interest
Lettermark Logo

```html
<!DOCTYPE html>
<html lang="en">
<head>
<meta charset="utf-8">
<title>KLD Business Card</title>
<link rel="stylesheet" href="https://fonts.googleapis.com/css2?family=Montserrat:wght@400;500;600;700&display=swap">
<style>
  :root {
    --stage: #2b2b2d;
    --card: #ffffff;
    --card-shade: #f1f1f1;
    --brand-red: #c9291d;
    --brand-orange: #e6702b;
    --brand-yellow: #f1b535;
    --ink: #4a4a4a;
    --band-text: #fbe9e6;
  }
  * { box-sizing: border-box; margin: 0; padding: 0; }
  html, body {
    width: 1200px;
    height: 901px;
    overflow: hidden;
    background: var(--stage);
    font-family: "Montserrat", Arial, sans-serif;
  }
  .sheet {
    width: 1200px;
    height: 901px;
    display: flex;
    flex-direction: column;
    align-items: center;
    justify-content: center;
    gap: 50px;
  }
  .card {
    width: 660px;
    height: 370px;
    background: var(--card);
    position: relative;
    overflow: hidden;
    box-shadow: 0 10px 30px rgba(0,0,0,0.45);
  }

  /* Back side */
  .card--back {
    background: linear-gradient(135deg, var(--card) 0%, var(--card-shade) 100%);
  }
  .back-texture {
    position: absolute;
    inset: 0;
    background: linear-gradient(160deg, rgba(230,230,230,0.0) 0%, rgba(220,220,220,0.55) 100%);
  }
  .back-mark {
    position: absolute;
    right: 70px;
    top: 50%;
    transform: translateY(-50%);
    display: flex;
    align-items: center;
    gap: 16px;
  }
  .back-mark__name {
    font-size: 96px;
    font-weight: 500;
    letter-spacing: 6px;
    color: var(--brand-red);
    line-height: 1;
  }
  .back-mark__dot {
    width: 18px;
    height: 18px;
    border-radius: 50%;
    background: var(--brand-yellow);
  }

  /* Front side */
  .card--front { padding: 38px 48px 0; }
  .front-mark {
    display: flex;
    align-items: center;
    gap: 12px;
  }
  .front-mark__name {
    font-size: 72px;
    font-weight: 500;
    letter-spacing: 5px;
    color: var(--brand-red);
    line-height: 1;
  }
  .front-mark__dot {
    width: 14px;
    height: 14px;
    border-radius: 50%;
    background: var(--brand-yellow);
  }
  .company {
    margin-top: 6px;
    font-size: 13px;
    font-weight: 600;
    color: var(--brand-red);
  }
  .person {
    margin-top: 22px;
    font-size: 27px;
    font-weight: 700;
    color: var(--brand-red);
    line-height: 1.1;
  }
  .job-title {
    font-size: 15px;
    font-weight: 500;
    color: var(--ink);
    margin-top: 2px;
  }
  .contacts {
    margin-top: 8px;
    display: grid;
    grid-template-columns: 62px auto;
    row-gap: 2px;
    font-size: 15px;
  }
  .contacts dt { font-weight: 700; color: var(--brand-red); }
  .contacts dd { font-weight: 500; color: var(--ink); }
  .address-band {
    position: absolute;
    left: 0;
    right: 0;
    bottom: 0;
    height: 50px;
    background: var(--brand-red);
    display: flex;
    align-items: center;
    padding-left: 48px;
    font-size: 14px;
    font-weight: 600;
    color: var(--band-text);
  }
</style>
</head>
<body>
<main class="sheet">
  <section class="card card--back" aria-label="Card back">
    <div class="back-texture" role="img" aria-label="Faint repeating tone-on-tone letter pattern"></div>
    <div class="back-mark">
      <span class="back-mark__name">KLD</span>
      <span class="back-mark__dot"></span>
    </div>
  </section>

  <section class="card card--front" aria-label="Card front">
    <div class="front-mark">
      <span class="front-mark__name">KLD</span>
      <span class="front-mark__dot"></span>
    </div>
    <p class="company">Marlowgate Property Collective Pty. Ltd.</p>
    <h1 class="person">Daniel Roke</h1>
    <p class="job-title">Licensed Real Estate Agent</p>
    <dl class="contacts">
      <dt>Mob</dt><dd>0437 592 046</dd>
      <dt>Phone</dt><dd>02 8364 5917</dd>
      <dt>Email</dt><dd>daniel.roke@marlowgatepc.com.au</dd>
    </dl>
    <div class="address-band">PO Box 732 Wendrick BC NSW 1593</div>
  </section>
</main>
</body>
</html>
```